Lantern Forge needs a business card

The logo we have uploaded is going to be the image centered on the back.
The business card color is going to be black. Increase the contrast in the logo and lettering so the grey stands out from the black and is more readable. Keep the shadow effect if you can.
On the front, the only part of the logo that should be used is the Egyptian character. We would like the following information included: Name (first last), Title, Phone number, email and company name (Lantern Forge).
The images of colored sound waves we uploaded is a concept we would like implemented on the front as well but please do not use the exact image. It is for guideline purposes.
Get creative with the empty space. We are a technology company that deals with sound and lights. Please not too busy.
Thank you, we look forward to all your submissions.

```html
<!DOCTYPE html>
<html lang="en">
<head>
<meta charset="utf-8">
<title>Lantern Forge — Business Card</title>
<link rel="stylesheet" href="https://fonts.googleapis.com/css2?family=Open+Sans:wght@400;600;700&display=swap">
<style>
  :root {
    --stage: #e9e7e4;
    --card-red: #ee2f37;
    --card-black: #2b2b2d;
    --card-edge: #8a8a8d;
    --ink-light: #ffffff;
    --ink-grey: #c9c9cc;
    --accent: #ee2f37;
  }
  * { box-sizing: border-box; margin: 0; padding: 0; }
  html, body {
    width: 1200px; height: 900px; overflow: hidden;
    background: var(--stage);
    font-family: "Open Sans", sans-serif;
  }
  .canvas {
    position: relative; width: 1200px; height: 900px;
    display: flex; flex-direction: column; align-items: center; justify-content: center; gap: 48px;
  }
  .card {
    position: relative; width: 640px; height: 366px;
    border-radius: 44px; overflow: hidden;
    box-shadow: 0 10px 28px rgba(0,0,0,0.18);
  }
  .card-front { background: var(--card-red); }
  .card-back { background: var(--card-black); display: flex; align-items: center; justify-content: center; }
  .front-shape { position: absolute; inset: 0; width: 100%; height: 100%; }
  .identity { position: absolute; left: 40px; top: 40px; color: var(--ink-light); }
  .identity-name { font-size: 24px; font-weight: 600; line-height: 1.2; }
  .identity-title { font-size: 15px; font-weight: 400; margin-top: 2px; }
  .contact-list { position: absolute; left: 40px; top: 168px; list-style: none; color: var(--ink-light); }
  .contact-item { display: flex; align-items: center; gap: 10px; font-size: 15px; line-height: 1; margin-bottom: 12px; }
  .contact-icon { width: 18px; height: 18px; flex: none; }
  .brand {
    position: absolute; display: flex; align-items: center; gap: 10px;
    color: var(--ink-grey); font-weight: 700; letter-spacing: 0.06em; text-transform: uppercase;
  }
  .brand-front { left: 372px; top: 160px; font-size: 24px; }
  .brand-back { position: static; font-size: 34px; }
  .brand-dot { border-radius: 50%; background: var(--accent); flex: none; }
  .brand-front .brand-dot { width: 14px; height: 14px; }
  .brand-back .brand-dot { width: 20px; height: 20px; }
</style>
</head>
<body>
<main class="canvas">
  <section class="card card-front" aria-label="Business card front">
    <svg class="front-shape" viewBox="0 0 640 366" aria-hidden="true">
      <path d="M640 0 H352 C286 0 264 46 264 120 V366 H640 Z" fill="var(--card-edge)"/>
      <path d="M640 0 H366 C302 0 280 50 280 122 V366 H640 Z" fill="var(--card-black)"/>
    </svg>
    <div class="identity">
      <p class="identity-name">Daniel Orsten</p>
      <p class="identity-title">Director</p>
    </div>
    <ul class="contact-list">
      <li class="contact-item">
        <svg class="contact-icon" viewBox="0 0 18 18" aria-hidden="true"><circle cx="9" cy="9" r="9" fill="#fff"/><path d="M6 5 L7.6 5 L8.2 7.2 L7.2 8 C7.7 9.2 8.8 10.3 10 10.8 L10.8 9.8 L13 10.4 L13 12 C9 12.4 5.6 9 6 5 Z" fill="var(--card-red)"/></svg>
        012 555 0143
      </li>
      <li class="contact-item">
        <svg class="contact-icon" viewBox="0 0 18 18" aria-hidden="true"><circle cx="9" cy="9" r="9" fill="#fff"/><rect x="6.5" y="4.5" width="5" height="9" rx="1" fill="var(--card-red)"/></svg>
        012 555 0143
      </li>
      <li class="contact-item">
        <svg class="contact-icon" viewBox="0 0 18 18" aria-hidden="true"><circle cx="9" cy="9" r="9" fill="#fff"/><rect x="4.5" y="6" width="9" height="6.5" fill="var(--card-red)"/><path d="M4.5 6 L9 9.6 L13.5 6" stroke="#fff" stroke-width="1" fill="none"/></svg>
        daniel@lanternforge.com
      </li>
    </ul>
    <div class="brand brand-front"><span class="brand-dot"></span>Lantern Forge</div>
  </section>

  <section class="card card-back" aria-label="Business card back">
    <div class="brand brand-back"><span class="brand-dot"></span>Lantern Forge</div>
  </section>
</main>
</body>
</html>
```